Clearway Lending Template Design

We need a corporate letterhead template (word) and slide show template (PowerPoint) designed for our Motor Vehicle finance business.

Clearway Lending provides motor vehicle finance to the credit impaired. Please feel free to visit our website www.clearwaylending-example.com

Both templates (word and PowerPoint) must include the Clearway logo (attached to this project) and can be very similar in design.

We are after something creative yet professional in design.

Please feel free to ask any questions.

Thank you
Marisol

```html
<!DOCTYPE html>
<html lang="en">
<head>
<meta charset="utf-8">
<title>Clearway Lending Letterhead</title>
<link rel="stylesheet" href="https://fonts.googleapis.com/css2?family=Cinzel:wght@400;700&display=swap">
<style>
  :root {
    --green: #1f8a3c;
    --green-tint: #dcefe1;
    --grey: #8a8b90;
    --grey-tint: #ececee;
    --ink: #4a4b52;
    --bar: #45474f;
    --paper: #ffffff;
  }
  html, body {
    margin: 0;
    padding: 0;
    overflow: hidden;
    background: var(--paper);
  }
  .letterhead {
    position: relative;
    width: 933px;
    height: 1200px;
    overflow: hidden;
    background: var(--paper);
    font-family: "Cinzel", "Times New Roman", serif;
  }
  .header-band {
    position: absolute;
    left: 0;
    top: 122px;
    width: 933px;
    height: 150px;
    background: linear-gradient(180deg, rgba(255,255,255,0) 0%, var(--paper) 100%),
                linear-gradient(90deg, var(--green-tint) 0%, var(--grey-tint) 60%, var(--green-tint) 100%);
  }
  .brand {
    position: absolute;
    left: 32px;
    top: 37px;
    display: flex;
    align-items: center;
    gap: 28px;
  }
  .brand-square {
    width: 90px;
    height: 90px;
    background: var(--grey);
  }
  .brand-name {
    font-weight: 700;
    font-size: 22px;
    line-height: 1;
    color: var(--green);
    white-space: nowrap;
  }
  .contact-column {
    position: absolute;
    top: 60px;
    height: 49px;
    border-left: 1.5px solid var(--green);
    display: flex;
    flex-direction: column;
    justify-content: space-between;
    padding: 3px 0 3px 18px;
    box-sizing: border-box;
    font-size: 10px;
    color: var(--ink);
  }
  .contact-column--identity { left: 420px; }
  .contact-column--reach { left: 647px; padding-left: 14px; }
  .contact-item {
    display: flex;
    align-items: center;
    gap: 9px;
    white-space: nowrap;
    height: 16px;
  }
  .contact-item svg {
    width: 12px;
    height: 12px;
    fill: var(--ink);
    flex: none;
  }
  .footer-bar {
    position: absolute;
    left: 0;
    top: 1115px;
    width: 933px;
    height: 9px;
    background: var(--bar);
  }
</style>
</head>
<body>
<main class="letterhead">
  <div class="header-band" role="img" aria-label="Soft green and grey header decoration"></div>

  <div class="brand">
    <div class="brand-square"></div>
    <div class="brand-name">Clearway Lending</div>
  </div>

  <div class="contact-column contact-column--identity">
    <div class="contact-item">
      <svg viewBox="0 0 12 12" aria-hidden="true"><circle cx="6" cy="3" r="2.6"/><path d="M1 12c0-3.2 2.2-5.2 5-5.2s5 2 5 5.2z"/></svg>
      <span>Clearway Lending</span>
    </div>
    <div class="contact-item">
      <svg viewBox="0 0 12 12" aria-hidden="true"><path d="M6 0a4.2 4.2 0 0 0-4.2 4.2C1.8 7.4 6 12 6 12s4.2-4.6 4.2-7.8A4.2 4.2 0 0 0 6 0zm0 6a1.8 1.8 0 1 1 0-3.6A1.8 1.8 0 0 1 6 6z"/></svg>
      <span>Clearway Lending</span>
    </div>
  </div>

  <div class="contact-column contact-column--reach">
    <div class="contact-item">
      <svg viewBox="0 0 12 12" aria-hidden="true"><path d="M2.4 0.6 4.2 2.8 3.2 4.3c.8 1.7 2.1 3 3.8 3.8l1.5-1 2.2 1.8-1 2.2C5.6 10.8 1.2 6.4.6 2.3z"/></svg>
      <span>000-000-0000</span>
    </div>
    <div class="contact-item">
      <svg viewBox="0 0 12 12" aria-hidden="true"><path d="M6 0a6 6 0 1 0 0 12A6 6 0 0 0 6 0zm4.4 5.2H8.6a9 9 0 0 0-.9-3.6 4.6 4.6 0 0 1 2.7 3.6zM6 1.3c.6.8 1.1 2.2 1.2 3.9H4.8C4.9 3.5 5.4 2.1 6 1.3zM4.3 1.6a9 9 0 0 0-.9 3.6H1.6a4.6 4.6 0 0 1 2.7-3.6zM1.6 6.8h1.8a9 9 0 0 0 .9 3.6 4.6 4.6 0 0 1-2.7-3.6zM6 10.7c-.6-.8-1.1-2.2-1.2-3.900h2.4c-.1 1.7-.6 3.1-1.2 3.9zm1.7-.3a9 9 0 0 0 .9-3.6h1.8a4.6 4.6 0 0 1-2.7 3.6z"/></svg>
      <span>www.clearwaylending-example.com</span>
    </div>
  </div>

  <div class="footer-bar"></div>
</main>
</body>
</html>
```